Harrowgate Estates Business Card for Apartment Buildings

Create business cards for resident managers who run apartment buildings. The audience is the public who are searching for apartment rentals, and current residents who live at the apartment building. Key design element will be incorporating the company logo, however, the logo cannot dominate. The building name and manager name are more important than the logo. Current business card design leaves little room for copy, so we may need to reduce the size on the current card to allow for more space for copy.

Target Market(s)

Adults 18-65 years of age, who are looking for an apartment rental, plus current residents who live at our apartment buildings.

Industry/Entity Type

Property Management

Contact Information for Business Card

A major design element will be use of the company logo. Important property and manager contact information must be part of the design. The size of the logo will need to be reduced to make room for building and manager contact copy.

Font styles to use
Sans Serif

Colors
3176b5
000000
959595
ffffff

Requirements
Must have
• 1) Incorporate the company logo.
• 2) Use the company colors (dark blue, black/grey, over white).
• 3) FEATURE THE BUILDING NAME
• 4) FEATURE THE MANAGER NAME
• 5) The company name is less important than BUILDING and MANAGER
• 6) Manager contact information
• **SEE ATTACHED CREATIVE BRIEF**
Nice to have
• 1) Back of card logo watermark
• 2) Ability to write notes on back of carfd
Should not have
• Avoid letting the company logo dominate the card, the building name and manager are more important than the company logo.

```html
<!DOCTYPE html>
<html lang="en">
<head>
<meta charset="utf-8">
<title>Harrowgate Estates – Resident Manager Card</title>
<link rel="stylesheet" href="https://fonts.googleapis.com/css2?family=Fira+Sans:wght@400;600&display=swap">
<style>
  :root {
    --brand-blue: #1f6db0;
    --ink: #3a3a3a;
    --rule: #555555;
    --band-dark: #48494d;
    --card: #ffffff;
    --backdrop: #e8e6e3;
    --ghost: #ececee;
  }
  * { margin: 0; padding: 0; box-sizing: border-box; }
  html, body { width: 1200px; height: 960px; overflow: hidden; }
  body {
    background: var(--backdrop);
    font-family: "Fira Sans", Arial, sans-serif;
    color: var(--ink);
    position: relative;
  }
  .card {
    position: absolute;
    left: 280px;
    width: 656px;
    height: 375px;
    background: var(--card);
    border-radius: 26px;
    overflow: hidden;
  }
  .card--front { top: 80px; }
  .card--back { top: 506px; }

  .ghost-circle {
    position: absolute;
    border-radius: 50%;
    background: var(--ghost);
  }
  .card--front .ghost-circle { width: 250px; height: 250px; left: 385px; top: 145px; }
  .card--back .ghost-circle { width: 250px; height: 250px; left: 205px; top: 55px; }

  .manager-name {
    position: absolute; left: 45px; top: 60px;
    font-size: 21px; font-weight: 600; color: var(--brand-blue);
  }
  .manager-title {
    position: absolute; left: 45px; top: 88px;
    font-size: 15.5px;
  }
  .company-mark {
    position: absolute; right: 36px; top: 52px;
    display: flex; align-items: center; gap: 10px;
  }
  .company-mark__square {
    width: 38px; height: 38px; background: var(--brand-blue);
  }
  .company-mark__name {
    font-size: 21px; font-weight: 600; color: var(--brand-blue);
    line-height: 1.1;
  }
  .building-name {
    position: absolute; left: 43px; top: 160px;
    font-size: 15px; font-weight: 600; color: var(--brand-blue);
  }
  .building-address {
    position: absolute; left: 43px; top: 183px;
    font-size: 15px;
  }
  .rule {
    position: absolute; left: 67px; width: 63px; height: 1px; background: var(--rule);
  }
  .rule--top { top: 204px; }
  .rule--bottom { top: 318px; }
  .contact-list {
    position: absolute; left: 43px; top: 227px; list-style: none;
  }
  .contact-list li {
    display: flex; align-items: center; height: 22.4px; font-size: 15px;
  }
  .contact-list svg { width: 16px; height: 16px; margin-right: 8px; fill: var(--brand-blue); }
  .website {
    position: absolute; left: 43px; top: 330px;
    font-size: 14px; letter-spacing: 3.2px;
  }
  .base-band {
    position: absolute; left: 0; right: 0; bottom: 0; height: 12px; background: var(--band-dark);
  }
  .base-band__accent {
    position: absolute; left: 39px; width: 217px; top: 0; bottom: 0;
    background: var(--brand-blue);
    border-left: 2px solid #fff; border-right: 2px solid #fff;
  }
</style>
</head>
<body>
  <section class="card card--front" aria-label="Card front">
    <div class="ghost-circle"></div>

    <h1 class="manager-name">Marisol Delgado</h1>
    <p class="manager-title">Resident Manager</p>

    <div class="company-mark">
      <span class="company-mark__square"></span>
      <span class="company-mark__name">Harrowgate Estates</span>
    </div>

    <h2 class="building-name">Cedar Court Apartments</h2>
    <p class="building-address">2485 Larkspur Avenue, San Diego, CA 92110</p>

    <div class="rule rule--top"></div>
    <ul class="contact-list">
      <li><svg viewBox="0 0 16 16"><path d="M4 1l3 3-2 2c1 2 3 4 5 5l2-2 3 3-2 3C7 15 1 9 2 3z"/></svg>555-210-4837</li>
      <li><svg viewBox="0 0 16 16"><path d="M2 4h12v3H2zM4 7h8v7H4zM6 9h1v1H6zm3 0h1v1H9zm-3 2h1v1H6zm3 0h1v1H9z"/></svg>555-210-4852</li>
      <li><svg viewBox="0 0 16 16"><path d="M4 1h8v14H4zM5.5 3v9h5V3zM7 13h2v1H7z" fill-rule="evenodd"/></svg>555-386-9014</li>
      <li><svg viewBox="0 0 16 16"><path d="M1 4h14v9H1zm1 1l6 4 6-4z" fill-rule="evenodd"/></svg>marisol@harrowgate.com</li>
    </ul>
    <div class="rule rule--bottom"></div>

    <p class="website">www.harrowgate.com</p>

    <div class="base-band"><div class="base-band__accent"></div></div>
  </section>

  <section class="card card--back" aria-label="Card back">
    <div class="ghost-circle"></div>
  </section>
</body>
</html>
```